Wine label

I'm wanting to create a wine label that is very very simple, but eye catching. Jump off the shelf.

Name of Winery : Marlow Ridge

Nothing on the front but that - will be putting other info on back - which will be the brand label.

I was thinking of something MR - possibly - with marlow ridge intertwined. -

1 color label and possible 1 or 2 ink

```html
<!DOCTYPE html>
<html lang="en">
<head>
<meta charset="utf-8">
<title>Marlow Ridge – wine label options</title>
<link rel="stylesheet" href="https://fonts.googleapis.com/css2?family=Barlow+Condensed:wght@500;600&display=swap">
<style>
  :root {
    --backdrop: #d6d6d6;
    --paper-white: #ffffff;
    --ink-black: #111111;
    --label-black: #000000;
    --orange: #e15724;
    --sky-blue: #1ca9df;
    --rule-red: #f1a39a;
    --rule-teal: #1a6a80;
    --caption: #ffffff;
  }
  html, body {
    margin: 0;
    padding: 0;
    width: 1200px;
    height: 1000px;
    overflow: hidden;
    background: var(--backdrop);
    font-family: "Barlow Condensed", "Arial Narrow", sans-serif;
  }
  .board {
    position: relative;
    width: 1200px;
    height: 1000px;
  }
  .option-caption {
    position: absolute;
    top: 24px;
    margin: 0;
    font-size: 32px;
    font-weight: 600;
    color: var(--caption);
    line-height: 1;
  }
  .option-caption--left { left: 32px; }
  .option-caption--right { right: 26px; }

  .label {
    position: absolute;
    top: 111px;
    width: 574px;
    height: 861px;
    box-shadow: 0 1px 4px rgba(0,0,0,0.35);
  }
  .label--light { left: 18px; background: var(--paper-white); }
  .label--dark { left: 607px; background: var(--label-black); }

  .colour-block {
    position: absolute;
    top: 185px;
    width: 490px;
    height: 491px;
  }
  .label--light .colour-block { left: 43px; background: var(--orange); color: var(--ink-black); }
  .label--dark .colour-block { left: 43px; background: var(--sky-blue); color: var(--paper-white); }

  .monogram {
    position: absolute;
    right: 52px;
    margin: 0;
    font-size: 292px;
    font-weight: 600;
    line-height: 1;
    text-align: right;
    letter-spacing: 2px;
  }
  .monogram__line { position: absolute; right: 0; white-space: nowrap; }
  .monogram__line--initials { top: -30px; }
  .monogram__line--year { top: 201px; }

  .base-rule {
    position: absolute;
    left: 2px;
    top: 718px;
    width: 558px;
    height: 2px;
  }
  .label--light .base-rule { background: var(--rule-red); }
  .label--dark .base-rule { background: var(--rule-teal); height: 1px; }

  .winery-name {
    position: absolute;
    right: 43px;
    top: 742px;
    margin: 0;
    font-size: 36px;
    font-weight: 600;
    line-height: 45px;
    letter-spacing: 6px;
    text-align: right;
    color: var(--ink-black);
    margin-right: -6px;
  }

  .wine-details {
    position: absolute;
    left: 19px;
    top: 27px;
    margin: 0;
    font-size: 30px;
    font-weight: 600;
    line-height: 32px;
    letter-spacing: 3px;
    color: var(--paper-white);
  }
</style>
</head>
<body>
  <main class="board">
    <p class="option-caption option-caption--left">option 5</p>
    <p class="option-caption option-caption--right">option 6</p>

    <section class="label label--light" aria-label="Option 5 label">
      <div class="colour-block">
        <h1 class="monogram">
          <span class="monogram__line monogram__line--initials">MR</span>
          <span class="monogram__line monogram__line--year">/08</span>
        </h1>
      </div>
      <div class="base-rule"></div>
      <p class="winery-name">Marlow<br>Ridge</p>
    </section>

    <section class="label label--dark" aria-label="Option 6 label">
      <div class="colour-block">
        <p class="wine-details">Marlow<br>Ridge<br>2008<br>Shiraz</p>
        <h2 class="monogram">
          <span class="monogram__line monogram__line--initials">MR</span>
          <span class="monogram__line monogram__line--year">/08</span>
        </h2>
      </div>
      <div class="base-rule"></div>
    </section>
  </main>
</body>
</html>
```